Creation of a cover for a book on popular ideas (received relief, preconceived ideas).
The picture (either photos or drawings) should represent a or several sheeps in a (French) city. The reason for this is that in France, people following general opinions are pictured as sheeps (following the herd )
Size: 11 x 17.8 cm
AUTHOR: Lucien-Mathis Vorrel
TITLE: Handbook of quiet garden walks
PUBLISHER: Korvane Editions (at the bottom of the page)

General adult public

Book

```html
<!DOCTYPE html>
<html lang="en">
<head>
<meta charset="utf-8">
<title>Handbook of quiet garden walks — Cover</title>
<link href="https://fonts.googleapis.com/css2?family=DM+Serif+Display&family=DM+Serif+Text&display=swap" rel="stylesheet">
<style>
  :root {
    --page: #ffffff;
    --cover-base: #7a6147;
    --sun: #fbe3a4;
    --street-warm: #c79a63;
    --street-mid: #9c7a55;
    --cream: #fdf6dc;
  }
  * { box-sizing: border-box; margin: 0; padding: 0; }
  html, body {
    width: 1200px;
    height: 1200px;
    overflow: hidden;
    background: var(--page);
  }
  .book-cover {
    position: absolute;
    left: 200px;
    top: 0;
    width: 800px;
    height: 1200px;
    background: var(--cover-base);
    box-shadow: 0 0 18px rgba(0,0,0,0.35);
    overflow: hidden;
  }
  .cover-photo {
    position: absolute;
    inset: 0 0 auto 0;
    height: 760px;
    background:
      radial-gradient(ellipse 180px 260px at 340px 60px, rgba(255,240,190,0.95), rgba(255,230,170,0) 100%),
      linear-gradient(90deg, rgba(90,55,40,0.75) 0%, rgba(90,55,40,0) 28%, rgba(90,55,40,0) 72%, rgba(120,90,60,0.45) 100%),
      linear-gradient(180deg, var(--sun) 0%, #e3b779 22%, var(--street-warm) 45%, var(--street-mid) 68%, var(--cover-base) 100%);
  }
  .cover-fade {
    position: absolute;
    left: 0; right: 0;
    top: 520px;
    height: 260px;
    background: linear-gradient(180deg, rgba(122,97,71,0) 0%, var(--cover-base) 100%);
  }
  .cover-title {
    position: absolute;
    left: 97px;
    top: 658px;
    font-family: "DM Serif Display", "DM Serif Text", Georgia, serif;
    font-weight: 400;
    font-size: 88px;
    line-height: 103px;
    letter-spacing: -0.5px;
    color: var(--cream);
  }
  .cover-author {
    position: absolute;
    left: 96px;
    top: 1094px;
    display: flex;
    align-items: center;
    gap: 22px;
  }
  .author-bar {
    width: 17px;
    height: 52px;
    background: var(--cream);
  }
  .author-name {
    font-family: "DM Serif Text", "DM Serif Display", Georgia, serif;
    font-size: 40px;
    line-height: 1;
    color: var(--cream);
  }
  .cover-publisher {
    position: absolute;
    right: 96px;
    bottom: 18px;
    font-family: "DM Serif Text", "DM Serif Display", Georgia, serif;
    font-size: 18px;
    line-height: 1;
    letter-spacing: 1px;
    color: var(--cream);
  }
</style>
</head>
<body>
  <div class="book-cover">
    <div class="cover-photo" role="img" aria-label="Photograph of a small flock of sheep walking down a sunlit cobbled street between old half-timbered French townhouses"></div>
    <div class="cover-fade"></div>
    <h1 class="cover-title">Handbook<br>of quiet<br>garden<br>walks</h1>
    <div class="cover-author">
      <span class="author-bar"></span>
      <span class="author-name">Lucien-Mathis Vorrel</span>
    </div>
    <p class="cover-publisher">Korvane Editions</p>
  </div>
</body>
</html>
```